High Quality Business card for Property Management Agency - Super Classy and professional design

High Quality Business card design.

We need a business card designed for our Property Management Agency.
We are located on Sydney's Northern Beaches and manage beautiful properties along the beach and harbor.
We need a design that oozes modern, classy and professional.
I would like it to be double sided with contact details and logo on the front and just the logo on the back.

I need a print ready PDF version of the file as well as an editable photoshop (PSD) version of the file.

Logo and information details attached.

Target Market(s)

Property owners/investors, Male and Female Aged 28-65

Industry/Entity Type

Real Estate

Contact Information for Business Card

Tom Carrick
Tel: 0467 239 018
Email: tom@harvestlaneestates.com.au
Website: www.harvestlaneestates.com.au
Address: Level 2, 17 Wattlecourt Rd, Dunmarra NSW 2187

Font styles to use
Sans Serif

Requirements
Must have
• - Logo front and back
• - Business card details listed above and attached
• - Colour
Nice to have
• Sleek and professional

```html
<!DOCTYPE html>
<html lang="en">
<head>
<meta charset="utf-8">
<title>Harvest Lane Estates – Business Card</title>
<link rel="stylesheet" href="https://fonts.googleapis.com/css2?family=Open+Sans:wght@400;600;700&display=swap">
<style>
  :root {
    --page-bg: #eceef0;
    --card-sky: #3cbfee;
    --card-edge: #1d5fa6;
    --wave-mid: #2a8fd2;
    --wave-navy: #1a56a3;
    --wave-pale: #bfeaf8;
    --wave-cyan: #6ae3f9;
    --ink: #16242d;
    --name-blue: #1e5ea8;
    --icon-blue: #1e4f93;
  }
  * { box-sizing: border-box; margin: 0; padding: 0; }
  html, body { width: 1200px; height: 860px; overflow: hidden; }
  body {
    background: var(--page-bg);
    font-family: "Open Sans", Arial, sans-serif;
    position: relative;
  }
  .card {
    position: absolute;
    width: 620px;
    height: 360px;
    background: var(--card-sky);
    border: 2px solid var(--card-edge);
    border-radius: 38px 38px 0 0;
    overflow: hidden;
    box-shadow: 0 10px 24px rgba(0,0,0,0.18);
  }
  .card-back { left: 60px; top: 50px; }
  .card-front { left: 520px; top: 450px; }
  .card-waves {
    position: absolute;
    left: 0; bottom: 0;
    width: 100%;
    height: 170px;
    z-index: 0;
  }
  .card-front .card-waves { height: 135px; }
  .brand-name, .holder-name, .contact-list, .website { z-index: 1; }
  .brand-name {
    position: absolute;
    color: var(--ink);
    font-weight: 600;
    letter-spacing: 0.5px;
    white-space: nowrap;
  }
  .card-back .brand-name {
    left: 0; right: 0;
    top: 128px;
    text-align: center;
    font-size: 44px;
  }
  .card-front .brand-name {
    right: 48px;
    top: 262px;
    font-size: 24px;
  }
  .holder-name {
    position: absolute;
    right: 52px;
    top: 36px;
    font-size: 42px;
    font-weight: 700;
    color: var(--name-blue);
    letter-spacing: 1px;
  }
  .contact-list {
    position: absolute;
    left: 56px;
    top: 112px;
    list-style: none;
  }
  .contact-item {
    display: flex;
    align-items: center;
    gap: 14px;
    height: 38px;
    font-size: 17px;
    color: var(--ink);
  }
  .contact-icon { width: 24px; height: 24px; fill: var(--icon-blue); flex: none; }
  .website {
    position: absolute;
    right: 40px;
    bottom: 18px;
    font-size: 16px;
    color: var(--ink);
  }
</style>
</head>
<body>

<section class="card card-back" aria-label="Card back">
  <svg class="card-waves" viewBox="0 0 620 170" preserveAspectRatio="none" aria-hidden="true">
    <path d="M0 120 C180 80 420 40 620 0 L620 170 L0 170 Z" fill="var(--wave-mid)"/>
    <path d="M0 135 C200 95 430 60 620 30 L620 170 L0 170 Z" fill="var(--card-sky)"/>
    <path d="M0 138 C200 98 430 62 620 32" stroke="var(--wave-navy)" stroke-width="7" fill="none"/>
    <path d="M0 155 C220 115 430 80 620 60 L620 170 L0 170 Z" fill="var(--wave-cyan)" opacity="0.85"/>
    <path d="M260 112 C400 80 520 60 620 48" stroke="var(--wave-pale)" stroke-width="4" fill="none"/>
  </svg>
  <p class="brand-name">HARVEST LANE ESTATES</p>
</section>

<section class="card card-front" aria-label="Card front">
  <svg class="card-waves" viewBox="0 0 620 170" preserveAspectRatio="none" aria-hidden="true">
    <path d="M0 40 C220 20 420 30 620 30 L620 170 L0 170 Z" fill="var(--wave-mid)"/>
    <path d="M300 40 C420 28 520 22 620 28" stroke="var(--wave-navy)" stroke-width="7" fill="none"/>
    <path d="M0 85 C200 90 420 70 620 60 L620 170 L0 170 Z" fill="var(--card-sky)"/>
    <path d="M0 78 C200 84 420 64 620 54" stroke="var(--wave-pale)" stroke-width="5" fill="none"/>
    <path d="M0 120 C220 115 430 95 620 85 L620 170 L0 170 Z" fill="var(--wave-cyan)" opacity="0.85"/>
  </svg>
  <h1 class="holder-name">Tom Carrick</h1>
  <ul class="contact-list">
    <li class="contact-item">
      <svg class="contact-icon" viewBox="0 0 24 24" aria-hidden="true"><path d="M12 3 L2 12 H5 V21 H10 V15 H14 V21 H19 V12 H22 Z"/></svg>
      <span>Level 2, 17 Wattlecourt Rd, Dunmarra NSW 2187</span>
    </li>
    <li class="contact-item">
      <svg class="contact-icon" viewBox="0 0 24 24" aria-hidden="true"><path d="M2 6 H22 V19 H2 Z M4 8 V17 H20 V8 L12 14 Z M5 7.5 L12 12.5 L19 7.5 Z"/></svg>
      <span>tom@harvestlaneestates.com.au</span>
    </li>
    <li class="contact-item">
      <svg class="contact-icon" viewBox="0 0 24 24" aria-hidden="true"><path d="M6.6 3 L9.5 6.5 L7.8 8.6 C8.8 11.2 10.6 13.5 13 15 L15 13.4 L18.6 16.2 L16.7 19.4 C10.2 18.5 4.9 12.7 4.3 5.6 Z"/></svg>
      <span>0467 239 018</span>
    </li>
  </ul>
  <p class="brand-name">HARVEST LANE ESTATES</p>
  <p class="website">www.harvestlaneestates.com.au</p>
</section>

</body>
</html>
```